Book Cover "Venice"

Creation of a cover (14 x 20.5 cm + bleed area) for a book:
Image: “BrumeVerte” (Tiff joined)
AUTHOR: Corinne Valmer
TITLE: The murmurs of Lorient
PUBLISHER: Editions Pluvane (AT THE BOTTOM OF THE COVER)

Target Market(s)

Readers of romantic novels

Industry/Entity Type

Book

```html
<!DOCTYPE html>
<html lang="fr">
<head>
<meta charset="utf-8">
<title>Les murmures de Lorient — Corinne Valmer</title>
<link rel="stylesheet" href="https://fonts.googleapis.com/css2?family=Antonio:wght@400;500&family=Playfair+Display:wght@400&display=swap">
<style>
  :root {
    --page-bg: #ffffff;
    --band-black: #050303;
    --gold: #c9a13a;
    --gold-deep: #a8822a;
    --sky-top: #a8151a;
    --sky-mid: #e0231c;
    --sky-glow: #e8341f;
    --dusk: #3a0806;
    --night: #0b0404;
    --title-shadow: #1a0a05;
  }
  * { margin: 0; padding: 0; box-sizing: border-box; }
  html, body {
    width: 1200px;
    height: 848px;
    overflow: hidden;
    background: var(--page-bg);
  }
  .canvas {
    position: relative;
    width: 1200px;
    height: 848px;
  }
  .book-cover {
    position: absolute;
    left: 320px;
    top: 14px;
    width: 561px;
    height: 820px;
    background: var(--band-black);
    overflow: hidden;
    box-shadow: 6px 6px 14px rgba(0,0,0,0.18);
  }
  .author-band {
    position: absolute;
    top: 0; left: 0; right: 0;
    height: 52px;
    background: var(--band-black);
    display: flex;
    align-items: center;
    justify-content: center;
  }
  .author-name {
    font-family: "Antonio", sans-serif;
    font-weight: 400;
    font-size: 21px;
    letter-spacing: 6px;
    color: var(--gold);
    text-transform: uppercase;
  }
  .cover-image {
    position: absolute;
    top: 52px; left: 0; right: 0;
    height: 748px;
    background:
      radial-gradient(ellipse 70% 30% at 50% 40%, var(--sky-glow) 0%, transparent 70%),
      linear-gradient(180deg,
        var(--sky-top) 0%,
        var(--sky-mid) 35%,
        var(--sky-mid) 55%,
        var(--dusk) 78%,
        var(--night) 100%);
  }
  .bottom-band {
    position: absolute;
    bottom: 0; left: 0; right: 0;
    height: 20px;
    background: var(--band-black);
  }
  .book-title {
    position: absolute;
    left: 0; top: 0;
    width: 100%;
    font-family: "Playfair Display", serif;
    font-weight: 400;
    color: var(--gold);
    text-shadow: 2px 2px 0 var(--title-shadow);
  }
  .title-line {
    position: absolute;
    white-space: nowrap;
    transform-origin: left bottom;
    line-height: 1;
  }
  .title-line--small {
    left: 84px;
    top: 138px;
    font-size: 104px;
    transform: scaleX(0.5);
  }
  .title-line--large {
    left: 52px;
    top: 212px;
    font-size: 196px;
    transform: scaleX(0.47);
  }
  .publisher {
    position: absolute;
    bottom: 38px;
    left: 0; right: 0;
    text-align: center;
    font-family: "Antonio", sans-serif;
    font-weight: 400;
    font-size: 15px;
    letter-spacing: 2.5px;
    color: var(--gold);
  }
</style>
</head>
<body>
  <main class="canvas">
    <article class="book-cover">
      <div class="cover-image" role="img" aria-label="Photographie : silhouettes de dômes et de lampadaires allumés sur un ciel de coucher de soleil rouge"></div>

      <header class="author-band">
        <p class="author-name">Corinne Valmer</p>
      </header>

      <h1 class="book-title">
        <span class="title-line title-line--small">Les murmures</span>
        <span class="title-line title-line--large">de Lorient</span>
      </h1>

      <p class="publisher">PUBLISHER: Editions Pluvane</p>

      <div class="bottom-band"></div>
    </article>
  </main>
</body>
</html>
```